Redesign web application

we are a tele health start up. we need a new design for our platform that allows users, their family and docs to access their detailed stats online
users take readings using our wireless devices that transmit the readings to our server in the background All this happens in real time . and users can instantly login to the portal to view readings , make comments, , view charts,
if readings are not within in prescribed thresholds then alerts are reported on the website, SMS and email
please see the screenshots of existing pages
We need the following pages re designed
login page
patient DB summary , patient DB condition
Doc DB
Nurse DB
After you submit designs and we choose the winning design . please help to make minor modifications after that so that we can use it
Target Market(s)
Paying
Doctors/ Clinics/Clinic chains/ Specialists will be the ones who are paying for the service. the service
Non Paying
patients family members, doctors all will be accessing the system to view readings, alerts , make comments , see charts
Industry/Entity Type
Health
Colors
Look and feel

```html
<!DOCTYPE html>
<html lang="en">
<head>
<meta charset="utf-8">
<title>VitaLinq – Patient DB Condition</title>
<link href="https://fonts.googleapis.com/css2?family=Lato:ital,wght@0,400;0,700;1,700&display=swap" rel="stylesheet">
<style>
:root{
  --blue:#5ba4d4;
  --blue-text:#4a9bd2;
  --green:#8dc63f;
  --ink:#222;
  --muted:#555;
  --panel:#eeeeee;
  --line:#dcdcdc;
  --footer:#333;
}
*{box-sizing:border-box;margin:0;padding:0}
html,body{width:1155px;height:1200px;overflow:hidden}
body{position:relative;font-family:'Lato',sans-serif;color:var(--ink);background:#fff;font-size:11px}
.abs{position:absolute}
a{color:inherit;text-decoration:none}

.site-header{position:absolute;left:0;top:0;width:1155px;height:59px;background:linear-gradient(#fff,#ececec);border-bottom:1px solid #ddd}
.brand{left:166px;top:12px;font-size:25px;font-weight:700;color:#111;letter-spacing:.3px}
.brand-mark{display:inline-block;width:14px;height:14px;border:2px solid #3a4fc1;margin-left:4px;vertical-align:2px}
.search{left:559px;top:20px;width:212px;height:24px;border:1px solid #ccc;border-radius:12px;background:#fff;padding:5px 14px;color:#bbb;font-size:11px}
.search svg{position:absolute;right:10px;top:5px}
.contact-box{left:790px;top:0;width:365px;height:59px;border-left:1px solid #ddd}
.contact{font-size:11px;color:#444;display:flex;align-items:center;gap:8px;position:absolute}

.main-nav{left:0;top:59px;width:1155px;height:35px;background:var(--blue);display:flex}
.main-nav a{position:absolute;top:0;height:35px;line-height:35px;color:#fff;font-size:13px;font-weight:700;text-align:center;border-right:1px solid #4c93c3}
.main-nav a.active{background:var(--green)}
.main-nav a.active::after{content:"";position:absolute;left:50%;bottom:-1px;margin-left:-4px;border:4px solid transparent;border-bottom-color:#fff}

.tabs{left:165px;top:127px;display:flex;gap:3px}
.tab{height:26px;line-height:26px;padding:0 13px;border:1px solid #ccc;border-bottom:none;background:#fff;color:var(--blue-text);font-size:12.5px}
.tab.current{background:#f0f0f0;color:#222;border-color:#f0f0f0;padding:0 26px}
.patient-card{left:165px;top:152px;width:825px;height:167px;border:1px solid #ccc;background:repeating-linear-gradient(135deg,#fafafa 0 3px,#f1f1f1 3px 5px)}
.photo{left:1px;top:12px;width:106px;height:128px;background:linear-gradient(160deg,#b9b9bd,#7a7f88 60%,#45495a)}
.field{position:absolute;font-size:11.5px;color:#222}
.val{position:absolute;font-size:11.5px;color:var(--blue-text)}
.val.name{color:var(--green);font-weight:700}
.comment-input{left:277px;top:45px;width:145px;height:21px;border:1px solid #ddd;background:#fff}
.date-input{position:absolute;height:20px;border:1px solid #ddd;background:#fff;padding:2px 5px;font-size:11.5px}
.btn{position:absolute;height:18px;line-height:18px;padding:0 6px;background:var(--blue);color:#fff;font-size:10.5px}

.side-menu{left:165px;top:340px;width:131px;height:230px;background:#ececec;box-shadow:1px 1px 3px rgba(0,0,0,.2)}
.side-menu li{list-style:none;height:33px;border-bottom:1px solid #ddd;display:flex;align-items:center;gap:10px;padding-left:8px;font-size:13px;color:#333}
.side-menu li:first-child{margin-top:7px}

.readings{left:328px;top:344px;width:313px;height:163px;background:var(--panel);border-radius:8px;overflow:hidden}
.readings .head{height:41px;border-bottom:4px solid var(--blue);display:flex;gap:20px;padding:14px 0 0 21px;font-size:13.5px;font-weight:700}
.row{height:24px;border-bottom:1px solid var(--line);text-align:center;line-height:24px;font-size:11px}
.row.first{height:30px;line-height:30px}

.box{position:absolute;left:678px;width:312px;background:var(--panel);border-radius:8px;overflow:hidden}
.box-head{height:41px;border-bottom:4px solid var(--blue);padding:14px 21px;font-size:13.5px;font-weight:700;position:relative}
.add{position:absolute;right:13px;top:15px;color:var(--blue-text);font-weight:400;font-size:11px}
.tools{position:absolute;right:26px;top:15px;display:flex;gap:14px}
.note-meta{font-size:10.5px;color:var(--green);padding:12px 0 0 14px}
.note-meta b{color:var(--blue-text)}
.note{font-size:11px;line-height:16px;color:#333;padding:6px 28px 0 15px}
.scroll{position:absolute;right:3px;top:45px;width:10px;bottom:5px;background:var(--blue)}
.scroll i{position:absolute;left:2px;top:10px;width:6px;height:13px;background:#fff}

.site-footer{left:0;top:1135px;width:1155px;height:65px;background:var(--footer);border-top:4px solid var(--blue)}
.site-footer p{position:absolute;left:168px;top:26px;color:#ddd;font-size:12px}
.social{position:absolute;right:165px;top:24px;display:flex;gap:11px}
.social span{width:15px;height:15px;border-radius:50%;background:#888}
</style>
</head>
<body>

<header class="site-header">
  <div class="abs brand">VitaLinq<span class="brand-mark"></span></div>
  <div class="abs search">Search:
    <svg width="14" height="14" viewBox="0 0 14 14"><circle cx="6" cy="6" r="4.5" fill="none" stroke="#111" stroke-width="2"/><path d="M9 9l4 4" stroke="#111" stroke-width="2"/></svg>
  </div>
  <div class="abs contact-box">
    <div class="contact" style="left:40px;top:13px">
      <svg width="14" height="12" viewBox="0 0 14 12"><path d="M2 1c2-1 3 2 2 3s1 4 3 5 2-1 3 0 2 2 0 2C5 12 0 5 2 1z" fill="var(--blue)"/></svg>
      Care Hotline (6100 2200)</div>
    <div class="contact" style="left:21px;top:32px">
      <svg width="15" height="11" viewBox="0 0 15 11"><rect x=".5" y=".5" width="14" height="10" fill="none" stroke="var(--blue)"/><path d="M.5.5l7 6 7-6" fill="none" stroke="var(--blue)"/></svg>
      help@vitalinq.example</div>
  </div>
</header>

<nav class="abs main-nav">
  <a style="left:165px;width:130px">DashBoard</a>
  <a style="left:295px;width:217px">Patient DB Summary</a>
  <a class="active" style="left:512px;width:212px">Patient DB Condition</a>
  <a style="left:724px;width:157px">Doc DB</a>
  <a style="left:881px;width:110px;border-right:none">Nurse DB</a>
</nav>

<div class="abs tabs">
  <div class="tab current">Summary</div>
  <div class="tab">Blood Pressure</div>
  <div class="tab">Blood Glucose</div>
  <div class="tab">Body Weight</div>
</div>

<section class="abs patient-card">
  <div class="abs photo" role="img" aria-label="Patient portrait photo"></div>
  <span class="field" style="left:147px;top:22px">Name of the Patient:</span>
  <span class="val name" style="left:278px;top:22px">Tan Wei Ling</span>
  <svg class="abs" style="left:410px;top:23px" width="12" height="12" viewBox="0 0 12 12"><rect x="1" y="2" width="8" height="9" fill="none" stroke="var(--blue)"/><path d="M5 7l6-6" stroke="var(--blue)" stroke-width="1.5"/></svg>
  <span class="field" style="left:147px;top:48px">Add General comment</span>
  <div class="abs comment-input"></div>
  <span class="field" style="left:147px;top:76px">Patient Type:</span>
  <span class="val" style="left:280px;top:77px">Surveillance</span>
  <span class="field" style="left:147px;top:101px">Primary Physician:</span>
  <span class="val" style="left:280px;top:102px">LIM KAH SOON</span>
  <span class="field" style="left:147px;top:125px">From:</span>
  <div class="date-input" style="left:180px;top:122px">2014-06-04</div>
  <span class="field" style="left:280px;top:125px">to:</span>
  <div class="date-input" style="left:297px;top:122px">2014-06-04</div>
  <div class="btn" style="left:393px;top:122px">Hosp Rep</div>
  <div class="btn" style="left:452px;top:122px">Pat Rep</div>
  <span class="field" style="left:648px;top:24px">NRIC #:</span>
  <span class="val" style="left:709px;top:24px">S1234H</span>
  <span class="field" style="left:635px;top:45px">Contact #:</span>
  <span class="val" style="left:709px;top:45px;line-height:14px">91230000 (HP),<br>61230000 (H/O)</span>
  <span class="field" style="left:595px;top:80px">Patient of Dept(s):</span>
  <span class="val" style="left:709px;top:80px">Cardio-AMI, UAT1</span>
</section>

<ul class="abs side-menu">
  <li><svg width="14" height="10" viewBox="0 0 14 10"><path d="M1 9a6 6 0 0 1 12 0" fill="none" stroke="#222" stroke-width="2"/><path d="M7 9l3-4" stroke="#222" stroke-width="2"/></svg>Site Usage</li>
  <li><svg width="14" height="10" viewBox="0 0 14 10"><rect width="14" height="10" fill="#222"/><path d="M0 0l7 5 7-5" fill="none" stroke="#eee"/></svg>Email</li>
  <li><svg width="14" height="12" viewBox="0 0 14 12"><rect x="5" y="0" width="4" height="4" fill="#222"/><rect x="0" y="8" width="4" height="4" fill="#222"/><rect x="5" y="8" width="4" height="4" fill="#222"/><rect x="10" y="8" width="4" height="4" fill="#222"/><path d="M2 8V6h10v2M7 4v4" fill="none" stroke="#222"/></svg>Doctors DB</li>
  <li><svg width="14" height="14" viewBox="0 0 14 14"><circle cx="5" cy="8" r="3.5" fill="none" stroke="#222" stroke-width="2.5" stroke-dasharray="2 1.2"/><circle cx="11" cy="3" r="2" fill="none" stroke="#222" stroke-width="1.6"/></svg>Settings</li>
  <li><svg width="14" height="12" viewBox="0 0 14 12"><path d="M.5 0v11.5H14" fill="none" stroke="#222"/><rect x="3" y="5" width="2" height="5" fill="#222"/><rect x="6" y="2" width="2" height="8" fill="#222"/><rect x="9" y="4" width="2" height="6" fill="#222"/></svg>View Chart</li>
  <li><svg width="14" height="14" viewBox="0 0 14 14"><path d="M4 3.5a5 5 0 1 0 6 0" fill="none" stroke="#222" stroke-width="2"/><path d="M7 1v6" stroke="#222" stroke-width="2"/></svg>Logout</li>
</ul>

<section class="abs readings">
  <div class="head"><span>Date</span><span>Time</span><span>Systolic</span><span>Diastolic</span><span>Pluset</span></div>
  <div class="row first">No Result found</div>
  <div class="row"></div>
  <div class="row"></div>
</section>

<section class="box" style="top:342px;height:220px">
  <div class="box-head">Standing Order BP<span class="add">+ Add Record</span></div>
  <div class="note-meta"><b>By UAT NURSE</b> &nbsp; on May 26 &nbsp;3:05 pm</div>
  <p class="note">Praesent nibh metus, porta sed metus eu, varius sodales nisl. Etiam ultrices sagittis eros ac semper. Maecenas eget blandit quam.</p>
  <p class="note" style="padding-top:16px">Suspendisse tincidunt augue nibh, eu cursus quam lacinia in. Nulla in bibendum leo. Nam interdum dictum diam ut dignissim. Nam quis nisl enim. Nam congue scelerisque pretium.</p>
  <div class="scroll"><i></i></div>
</section>

<section class="box" style="top:583px;height:136px">
  <div class="box-head">Confidential Patient Notes BP<span class="add">+ Add Record</span></div>
  <div class="note-meta"><b>By UAT NURSE</b> &nbsp; on May 26 &nbsp;3:07 pm</div>
  <p class="note" style="padding-right:12px">Praesent nibh metus, porta sed metus eu, varius sodales nisl. Etiam ultrices sagittis eros ac semper. Maecenas eget blandit quam.</p>
</section>

<section class="box" style="top:747px;height:163px">
  <div class="box-head">Blood Pressure
    <span class="tools">
      <svg width="11" height="11" viewBox="0 0 12 12"><path d="M2 6a4 4 0 0 1 7-3M10 6a4 4 0 0 1-7 3" fill="none" stroke="#222" stroke-width="1.6"/><path d="M9 0v3.5H5.5M3 12V8.5h3.5" fill="none" stroke="#222" stroke-width="1.4"/></svg>
      <svg width="11" height="11" viewBox="0 0 11 11"><rect x=".5" y="1.5" width="10" height="9" fill="none" stroke="#222"/><path d="M.5 4h10M3 0v3M8 0v3M3 6h5M3 8h5" stroke="#222"/></svg>
      <svg width="9" height="9" viewBox="0 0 9 9"><path d="M1 1l7 7M8 1L1 8" stroke="#222" stroke-width="2"/></svg>
    </span></div>
  <div class="row first">No Data Available</div>
  <div class="row"></div>
  <div class="row"></div>
</section>

<section class="box" style="top:937px;height:163px">
  <div class="box-head">Pluse
    <span class="tools">
      <svg width="11" height="11" viewBox="0 0 12 12"><path d="M2 6a4 4 0 0 1 7-3M10 6a4 4 0 0 1-7 3" fill="none" stroke="#222" stroke-width="1.6"/><path d="M9 0v3.5H5.5M3 12V8.5h3.5" fill="none" stroke="#222" stroke-width="1.4"/></svg>
      <svg width="11" height="11" viewBox="0 0 11 11"><rect x=".5" y="1.5" width="10" height="9" fill="none" stroke="#222"/><path d="M.5 4h10M3 0v3M8 0v3M3 6h5M3 8h5" stroke="#222"/></svg>
      <svg width="9" height="9" viewBox="0 0 9 9"><path d="M1 1l7 7M8 1L1 8" stroke="#222" stroke-width="2"/></svg>
    </span></div>
  <div class="row first">No Data Available</div>
  <div class="row"></div>
  <div class="row"></div>
</section>

<footer class="abs site-footer">
  <p>© 2014 vitalinq.example All Rights reserved</p>
  <div class="social"><span></span><span></span><span></span><span></span></div>
</footer>

</body>
</html>
```